Business Card Design Project

We are rebranding an existing automotive collision repair business. The business is called dentworks garage. I have attached logo but I'm not tied to that. I want to leave this wide open.

I want this card to say we are professional, competent, cutting edge. We are focused on customers and use a lot of the latest technology to make the customer experience different. We sign customers in on iPads. Paperwork I signed electronically and updates are sent via text, email, logging on a website or as they wish. I want this innovation and image to come through in our cards

Target Market(s)

60%. Women 40% men. Age 35-60

Industry/Entity Type

Automotive

Requirements
Must have
• The card must have name, title, phone,email, cell, web page

```html
<!DOCTYPE html>
<html lang="en">
<head>
<meta charset="utf-8">
<title>Dentworks Garage – Business Card</title>
<link rel="stylesheet" href="https://fonts.googleapis.com/css2?family=Arimo:wght@400;700&display=swap">
<style>
  :root {
    --backdrop: #e6e7e9;
    --card-white: #ffffff;
    --card-grey: #a7a8ab;
    --brand-green: #617d37;
    --brand-lime: #a9d45c;
    --ink-dark: #2b2b2d;
    --ink-soft: #f2f2f2;
  }
  * { box-sizing: border-box; margin: 0; padding: 0; }
  html, body {
    width: 1200px; height: 800px; overflow: hidden;
    background: var(--backdrop);
    font-family: "Arimo", Arial, sans-serif;
  }
  .canvas { position: relative; width: 1200px; height: 800px; }
  .card {
    position: absolute; top: 110px;
    width: 289px; height: 504px;
    border-radius: 14px; overflow: hidden;
  }
  .card--front { left: 209px; background: var(--card-white); }
  .card--back { left: 705px; background: var(--card-grey); }

  .brand-band {
    position: absolute; left: 40px; top: 291px;
    width: 249px; height: 85px;
    background: var(--brand-green);
    border-radius: 42.5px 0 0 42.5px;
    display: flex; align-items: center; justify-content: center;
    padding-left: 14px;
  }
  .brand-name {
    color: var(--brand-lime);
    font-weight: 700; font-size: 21px; letter-spacing: -0.2px;
    white-space: nowrap;
  }
  .front-web {
    position: absolute; left: 40px; top: 375px; width: 249px;
    text-align: center; color: var(--brand-green);
    font-size: 16px; line-height: 20px; white-space: nowrap;
  }

  .accent-tab {
    position: absolute; left: 0; top: 291px;
    width: 50px; height: 85px;
    background: var(--brand-green);
    border-radius: 0 42.5px 42.5px 0;
  }
  .person { position: absolute; left: 63px; top: 316px; }
  .person-name { color: var(--ink-dark); font-weight: 700; font-size: 19px; line-height: 22px; }
  .person-title { color: var(--ink-soft); font-size: 15px; line-height: 18px; }

  .contact-list { position: absolute; left: 62px; top: 381px; list-style: none; }
  .contact-item {
    display: flex; align-items: center; height: 26.5px;
    color: var(--ink-soft); font-size: 15.5px; white-space: nowrap;
  }
  .contact-icon { width: 18px; height: 18px; margin-right: 12px; flex: none; }
  .contact-icon * { fill: none; stroke: var(--ink-soft); stroke-width: 1.3; }
</style>
</head>
<body>
<div class="canvas">

  <section class="card card--front" aria-label="Card front">
    <div class="brand-band">
      <span class="brand-name">Dentworks Garage</span>
    </div>
    <p class="front-web">www.dentworks.com</p>
  </section>

  <section class="card card--back" aria-label="Card back">
    <div class="accent-tab"></div>
    <div class="person">
      <p class="person-name">Marcus Hale</p>
      <p class="person-title">Director</p>
    </div>
    <ul class="contact-list">
      <li class="contact-item">
        <svg class="contact-icon" viewBox="0 0 18 18"><rect x="1.5" y="4" width="15" height="10"/><path d="M1.5 4l7.5 6 7.5-6M1.5 14l5.5-5M16.5 14l-5.5-5"/></svg>
        abcde@dentworks.com
      </li>
      <li class="contact-item">
        <svg class="contact-icon" viewBox="0 0 18 18"><circle cx="9" cy="9" r="7.5"/><ellipse cx="9" cy="9" rx="3.2" ry="7.5"/><path d="M1.5 9h15M3 5h12M3 13h12"/></svg>
        www.dentworks.com
      </li>
      <li class="contact-item">
        <svg class="contact-icon" viewBox="0 0 18 18"><path d="M4 2l3 3.2-1.6 2a10 10 0 0 0 5.4 5.4l2-1.6L16 14l-2 2.2C8 15.8 2.2 10 1.8 4z"/></svg>
        +1 (800) 555-0142
      </li>
      <li class="contact-item">
        <svg class="contact-icon" viewBox="0 0 18 18"><rect x="5" y="1.5" width="8" height="15" rx="1.2"/><path d="M8 14h2"/></svg>
        +1 (800) 555-0142
      </li>
    </ul>
  </section>

</div>
</body>
</html>
```